Corvane Electronics, Inc. Business card

Incorporate a globe.
We repair electronics, sell electronic parts, and we recycle electronics. We've been in business since 1982. A technology feel to the card is preferred. I want to be able to give this card to a client from different industries and make it relate-able. I don't have a logo that I've been partial to in the past. It is not necessary in this case.

Target Market(s)

Consumer, Industrial, Business, Medical

Industry/Entity Type

Business

Contact Information for Business Card

4518 Maple Crest Blvd. Alder Ridge, TX 75099
214-555-0187 main 214-555-0143 fax
Paul Bredesen VP

Font styles to use
Serif

Requirements
Must have
• Technology feel
Nice to have
• Metallic look
Should not have
• no pastel colors

```html
<!DOCTYPE html>
<html lang="en">
<head>
<meta charset="utf-8">
<title>Corvane Electronics, Inc. — Business Card</title>
<link href="https://fonts.googleapis.com/css2?family=Exo+2:wght@400;500;600&display=swap" rel="stylesheet">
<style>
  :root {
    --page: #ffffff;
    --card-black: #0b0c0e;
    --card-charcoal: #1c1f24;
    --silver-light: #f4f5f6;
    --silver-mid: #c9cbce;
    --silver-dark: #9a9da2;
    --brand-blue: #2d62c4;
    --brand-blue-bright: #3f7ee8;
    --text-light: #e9ebee;
    --divider: #5b6068;
  }
  * { box-sizing: border-box; margin: 0; padding: 0; }
  html, body {
    width: 1200px; height: 900px; overflow: hidden;
    background: var(--page);
    font-family: "Exo 2", sans-serif;
  }
  .stage {
    width: 1200px; height: 900px;
    display: flex; align-items: center; justify-content: center; gap: 44px;
  }
  .card {
    width: 540px; height: 320px;
    border-radius: 26px;
    overflow: hidden;
    position: relative;
    box-shadow: 0 18px 40px rgba(0,0,0,0.22);
  }
  /* Front */
  .card-front {
    background: radial-gradient(ellipse at 30% 45%, var(--card-charcoal) 0%, var(--card-black) 70%);
  }
  .wordmark {
    display: flex; align-items: center; gap: 12px;
    color: var(--brand-blue-bright);
    font-weight: 600;
    letter-spacing: 0.04em;
    text-transform: uppercase;
    white-space: nowrap;
  }
  .wordmark-dot {
    border-radius: 50%;
    background: radial-gradient(circle at 35% 35%, #dfe3e8 0%, #6f7f98 45%, #1b2333 100%);
    flex: none;
  }
  .card-front .wordmark {
    position: absolute; left: 92px; top: 132px;
    font-size: 20px;
  }
  .card-front .wordmark-dot { width: 56px; height: 56px; }

  /* Back */
  .card-back { background: var(--card-black); }
  .back-top {
    height: 168px;
    background: linear-gradient(180deg, var(--silver-light) 0%, var(--silver-mid) 65%, var(--silver-dark) 100%);
    display: flex; align-items: center; justify-content: center;
  }
  .card-back .wordmark { font-size: 19px; color: var(--brand-blue); }
  .card-back .wordmark-dot { width: 52px; height: 52px; }
  .accent-band {
    height: 7px;
    background: linear-gradient(90deg, var(--brand-blue) 0%, var(--brand-blue-bright) 50%, var(--brand-blue) 100%);
    border-bottom: 2px solid var(--silver-mid);
  }
  .back-bottom {
    height: 143px;
    background: linear-gradient(180deg, var(--card-charcoal) 0%, var(--card-black) 100%);
    display: flex; align-items: center; padding: 0 20px 0 0;
  }
  .person {
    width: 200px; flex: none; text-align: right; padding-right: 14px;
  }
  .person-name { color: var(--brand-blue-bright); font-size: 18px; font-weight: 500; white-space: nowrap; }
  .person-title { color: var(--text-light); font-size: 12px; margin-top: 4px; }
  .contact-list {
    list-style: none;
    border-left: 1px solid var(--divider);
    padding-left: 10px;
    display: flex; flex-direction: column; gap: 3px;
  }
  .contact-item {
    display: flex; align-items: center; gap: 6px;
    color: var(--text-light); font-size: 12px; line-height: 1.25;
    white-space: nowrap;
  }
  .contact-icon { width: 12px; height: 12px; flex: none; fill: var(--brand-blue-bright); }
</style>
</head>
<body>
<main class="stage">
  <section class="card card-front" aria-label="Business card front">
    <div class="wordmark">
      <span class="wordmark-dot"></span>
      <span class="wordmark-name">Corvane Electronics, Inc.</span>
    </div>
  </section>

  <section class="card card-back" aria-label="Business card back">
    <div class="back-top">
      <div class="wordmark">
        <span class="wordmark-dot"></span>
        <span class="wordmark-name">Corvane Electronics, Inc.</span>
      </div>
    </div>
    <div class="accent-band"></div>
    <div class="back-bottom">
      <div class="person">
        <p class="person-name">Paul Bredesen VP</p>
        <p class="person-title">Manager</p>
      </div>
      <ul class="contact-list">
        <li class="contact-item">
          <svg class="contact-icon" viewBox="0 0 12 12"><rect x="3" y="0.5" width="6" height="11" rx="1.2"/><rect x="4" y="2" width="4" height="6.5" fill="#0b0c0e"/></svg>
          214-555-0187
        </li>
        <li class="contact-item">
          <svg class="contact-icon" viewBox="0 0 12 12"><path d="M2.3 0.8l2 2.2-1 1.4c.7 1.6 2 2.9 3.6 3.6l1.4-1 2.2 2-1.2 2C5.3 10.6 1.4 6.7.7 2z"/></svg>
          214-555-0143
        </li>
        <li class="contact-item">
          <svg class="contact-icon" viewBox="0 0 12 12"><rect x="0.5" y="2.5" width="11" height="7" rx="0.8"/><path d="M1 3l5 3.6L11 3" fill="none" stroke="#0b0c0e" stroke-width="1"/></svg>
          paul@corvaneelectronics.com
        </li>
        <li class="contact-item">
          <svg class="contact-icon" viewBox="0 0 12 12"><circle cx="6" cy="6" r="5.3" fill="none" stroke="#3f7ee8" stroke-width="1.1"/><ellipse cx="6" cy="6" rx="2.2" ry="5.3" fill="none" stroke="#3f7ee8" stroke-width="1"/><path d="M0.8 6h10.4" stroke="#3f7ee8" stroke-width="1"/></svg>
          corvaneelectronics.com
        </li>
        <li class="contact-item">
          <svg class="contact-icon" viewBox="0 0 12 12"><path d="M6 0.8L0.5 6h1.7v5h3V8h1.6v3h3V6h1.7z"/></svg>
          4518 Maple Crest Blvd. Alder Ridge, TX 75099
        </li>
      </ul>
    </div>
  </section>
</main>
</body>
</html>
```